bold, classy, clean design for legal stationary and business cards - more modern than traditional
New law office stationary, that looks like the firm is bold, successful, professional, and not new.
bold, classy, clean design for legal stationary and business cards - more modern than traditional - Law
Creative Brief
Professional
Tess R. Ford
Law Office of Tess R. Ford, LLC 47 W. Harlow Avenue, Suite 315 Chicago, IL 60699
Office - 312-555-0148
Mobile - 773-555-0172
trf@tessfordcounsel.example
www.tessfordcounsel.example
I have purchased a logo, and I hope that I attach the correct format. I am a new company, so I am trying to be cost conscious, yet have the card look like a million bucks. The logo is red and dark grey. I would like to keep the card to just those colors, and only have red on the front, I hope that saves money. If you think the type should be black rather than dark grey, I am OK with that. The back side (I think) should just be black or dark grey. I would like something professional and bold.
I would like these four areas of practice on the back of the card: personal injury wrongful death medical malpractice auto accidents perhaps putting a dash/diamond/line in-between the words
tessfordcounsel tessfordcounsel
Can you please show me stationary designs for letterhead and envelopes.

```html
<!DOCTYPE html>
<html lang="en">
<head>
<meta charset="utf-8">
<title>Tess R. Ford — Business Card</title>
<link rel="stylesheet" href="https://fonts.googleapis.com/css2?family=Cinzel:wght@400;600&display=swap">
<style>
  :root {
    --page-bg: #e9e6e3;
    --card-white: #fbfbfb;
    --brand-red: #c42a3c;
    --brand-red-dark: #a81f30;
    --ink-grey: #3b3b3d;
    --rule-grey: #b9b9bb;
    --card-shadow: rgba(0, 0, 0, 0.18);
  }
  * { box-sizing: border-box; margin: 0; padding: 0; }
  html, body {
    width: 1200px; height: 871px; overflow: hidden;
    background: var(--page-bg);
    font-family: "Cinzel", "Times New Roman", serif;
  }
  .sheet {
    width: 1200px; height: 871px;
    display: flex; flex-direction: column; align-items: center; justify-content: center;
    gap: 56px;
  }
  .card {
    position: relative;
    width: 630px; height: 360px;
    box-shadow: 0 10px 26px var(--card-shadow);
  }

  /* ---------- back ---------- */
  .card--back { background: var(--brand-red); color: #fff; }
  .card--back .lockup { position: absolute; left: 150px; top: 96px; display: flex; align-items: center; gap: 20px; }
  .card--back .lockup-mark { width: 66px; height: 66px; border: 3px solid #fff; }
  .card--back .lockup-name { color: #fff; }
  .card--back .practice-heading {
    position: absolute; left: 0; right: 0; top: 218px;
    display: flex; align-items: center; justify-content: center; gap: 18px;
    font-size: 15px; letter-spacing: 3px;
  }
  .practice-heading .rule { width: 90px; height: 1px; background: rgba(255,255,255,0.7); }

  /* ---------- front ---------- */
  .card--front { background: var(--card-white); color: var(--ink-grey); }
  .card--front .lockup { position: absolute; left: 238px; top: 40px; display: flex; align-items: center; gap: 16px; }
  .card--front .lockup-mark { width: 62px; height: 62px; background: var(--brand-red); }
  .card--front .lockup-name { color: var(--brand-red); }

  .lockup-name { font-weight: 400; line-height: 1.05; }
  .lockup-name .small { display: block; font-size: 14px; letter-spacing: 3px; }
  .lockup-name .large { display: block; font-size: 30px; letter-spacing: 1px; }

  .divider { position: absolute; left: 238px; top: 140px; width: 1px; height: 196px; background: var(--rule-grey); }

  .holder-name {
    position: absolute; left: 34px; top: 222px;
    font-size: 25px; font-weight: 400; color: var(--ink-grey);
  }

  .address {
    position: absolute; left: 258px; top: 140px;
    font-size: 15px; line-height: 1.4; color: var(--ink-grey);
  }

  .contacts { position: absolute; left: 258px; top: 236px; list-style: none; font-size: 12.5px; color: var(--ink-grey); }
  .contacts li { display: flex; align-items: center; gap: 10px; height: 22px; }
  .contact-icon { width: 15px; height: 15px; flex: none; }
</style>
</head>
<body>
<main class="sheet">

  <section class="card card--back" aria-label="Card back">
    <div class="lockup">
      <div class="lockup-mark"></div>
      <div class="lockup-name"><span class="small">Law Office of</span><span class="large">Tess R. Ford</span></div>
    </div>
    <div class="practice-heading"><span class="rule"></span>Areas of Practice<span class="rule"></span></div>
  </section>

  <section class="card card--front" aria-label="Card front">
    <div class="lockup">
      <div class="lockup-mark"></div>
      <div class="lockup-name"><span class="small">Law Office of</span><span class="large">Tess R. Ford</span></div>
    </div>

    <div class="divider"></div>
    <h1 class="holder-name">Tess R. Ford</h1>

    <address class="address" style="font-style:normal">
      Law Office of Tess R. Ford, LLC<br>
      47 W. Harlow Avenue, Suite 315<br>
      Chicago, IL 60699
    </address>

    <ul class="contacts">
      <li>
        <svg class="contact-icon" viewBox="0 0 16 16"><circle cx="8" cy="8" r="8" fill="var(--brand-red)"/><path d="M5.2 4.3l1.4-.3.7 1.8-.9.6c.4 1 1.2 1.8 2.2 2.2l.6-.9 1.8.7-.3 1.4c-3 .2-5.7-2.5-5.5-5.5z" fill="#fff"/></svg>
        312-555-0148
      </li>
      <li>
        <svg class="contact-icon" viewBox="0 0 16 16"><circle cx="8" cy="8" r="8" fill="var(--brand-red)"/><rect x="5.6" y="3.6" width="4.8" height="8.8" rx="0.8" fill="#fff"/><rect x="6.3" y="4.6" width="3.4" height="5.8" fill="var(--brand-red)"/></svg>
        773-555-0172
      </li>
      <li>
        <svg class="contact-icon" viewBox="0 0 16 16"><circle cx="8" cy="8" r="8" fill="var(--brand-red)"/><rect x="4" y="5.2" width="8" height="5.6" fill="#fff"/><path d="M4 5.2l4 3 4-3" fill="none" stroke="var(--brand-red)" stroke-width="0.9"/></svg>
        trf@tessfordcounsel.example
      </li>
      <li>
        <svg class="contact-icon" viewBox="0 0 16 16"><circle cx="8" cy="8" r="8" fill="var(--brand-red)"/><circle cx="8" cy="8" r="4" fill="none" stroke="#fff" stroke-width="0.9"/><path d="M4 8h8M8 4c-1.6 2.4-1.6 5.6 0 8M8 4c1.6 2.4 1.6 5.6 0 8" fill="none" stroke="#fff" stroke-width="0.8"/></svg>
        www.tessfordcounsel.example
      </li>
    </ul>
  </section>

</main>
</body>
</html>
```